Modern and sophisticated web design for architect/designer

Vantor Loom is a Building Design & Drafting studio based in Nedlands Western Australia, providing a high quality and complete client service from concept design through Council planning approvals and building licenses to construction drawings for kitchens and bathrooms, extensions, additions, renovations and new homes.

Vantor Loom is looking for a new qwerty design that *is different from a normal* 2/3 column website. The website design must be very arty, clean and catchy. This design needs to be very different and must not look like a downloadable template.

The design must be able to display a lot of photos for the different projects.

The design must comply with W3C standards (i.e. use of fonts) and must be delivered to us in A PSD layered format.

Here are a couple of example website designs that exemplify what I am after:
1) http://www.plvm.com.au/
2) http://www.thomasvellearchitect.com/en/
3) http://quormel.com/

I particularly like numbers 1 and 2. The third, Quormel, jumps around a little between pages as it is actually several companies. I prefer the page design to remain steady if possible.

I like the very clever nature of number 1 (PLVM). It captures the interest, although slightly gimmicky, however I think it doesn't overpower. Its modern, and visual.

I like the clean elegant design of number 2 (Velle), it simply delivers everything necessary in a clear intelligent manner, its attractive, menu is clever simple to use and attractive.

I would be very happy to have either of these websites.

here is another one:
4) http://www.wnarchitect.com.au/

Although this is similarly elegant, it appears quite dated. I don't like the thumbnails that you click on in the gallery, its quite clumsy. It looks minimalist, and IS minimalist, doesn't look like there is much option to expand other than changing the pictures.

If you look at my own website:
http://www.vantorloom.com.au

I designed and built it myself without any skills or experience. I had to use a generic photo album generator which was worse than useless, the point I am trying to make is I tried to make the menu system a little unusual, I tried to keep the pages neat and tidy, and totally used the "black website" method. However I am more inclined to go with the lighter/white pages of (1) and (2) above because they tend to show photos better.
Updates

Dear Designers. 

ArtBazaarHub Administration has worked to provide a more comprehensive brief. Please review the amended description. 

Kind Regards, Gordon. 

Target Market(s)

Target market is people who are looking to renovate their home

Industry/Entity Type

Construction

Requirements
Must have
• The brief is to design a visual modern, elegant, sophisticated website for a small scale designer/photographer/architect that looks itself like it is designed. Not off the shelf, simple and dated. Basically the design itself has to exemplify me, it has to say "this guy is a designer, and he is good at it".

```html
<!DOCTYPE html>
<html lang="en">
<head>
<meta charset="utf-8">
<title>Vantor Loom Design — Building Design &amp; Drafting Studio</title>
<link rel="stylesheet" href="https://fonts.googleapis.com/css2?family=Jost:wght@500;600&family=Questrial&family=Days+One&display=swap">
<style>
  :root {
    --ink: #000000;
    --nav-active: #ffffff;
    --nav-idle: #a9a9a9;
    --band: #a3a3a3;
    --panel-top: #ebebeb;
    --panel-bottom: #bdbdbd;
    --heading: #3a3a3a;
    --body-text: #454545;
    --section-title: #555555;
    --frame: #f2f2f2;
    --card: #dcdcdc;
    --arrow: #9a9a9a;
    --footer-text: #dddddd;
  }
  * { margin: 0; padding: 0; box-sizing: border-box; }
  html, body { width: 1200px; height: 773px; overflow: hidden; background: var(--ink); }
  .page { position: relative; width: 1200px; height: 773px; overflow: hidden; font-family: Arial, Helvetica, sans-serif; }

  .site-nav { position: absolute; left: 0; top: 0; width: 1200px; height: 44px; background: var(--ink); }
  .site-nav a { position: absolute; top: 11px; font-family: "Jost", sans-serif; font-weight: 600; font-size: 17px; letter-spacing: .3px; color: var(--nav-idle); text-decoration: none; text-transform: uppercase; }
  .site-nav a.is-active { color: var(--nav-active); }
  .nav-pointer { position: absolute; left: 162px; top: 36px; width: 0; height: 0; border-left: 9px solid transparent; border-right: 9px solid transparent; border-bottom: 8px solid var(--band); }
  .social-links { position: absolute; right: 16px; top: 8px; display: flex; gap: 9px; }
  .social-links span { width: 27px; height: 27px; border-radius: 50%; background: var(--nav-active); display: block; }

  .top-band { position: absolute; left: 0; top: 44px; width: 1200px; height: 38px; background: var(--band); }
  .main-panel { position: absolute; left: 0; top: 82px; width: 1200px; height: 556px; background: linear-gradient(180deg, var(--panel-top), var(--panel-bottom)); border-right: 2px solid #9a9a9a; }
  .bottom-band { position: absolute; left: 0; top: 638px; width: 1200px; height: 15px; background: var(--band); }

  .brand { position: absolute; left: 18px; top: 186px; display: flex; align-items: center; gap: 16px; }
  .brand-mark { width: 22px; height: 22px; background: var(--ink); }
  .brand-name { font-family: "Jost", sans-serif; font-weight: 600; font-size: 54px; letter-spacing: 3px; color: var(--ink); text-transform: uppercase; line-height: 1.05; }

  .studio-title { position: absolute; left: 28px; top: 356px; font-family: "Questrial", sans-serif; font-size: 35px; font-weight: 400; color: var(--heading); letter-spacing: -.3px; }
  .studio-intro { position: absolute; left: 28px; top: 418px; width: 520px; font-size: 15.6px; line-height: 20.3px; color: var(--body-text); }

  .section-title { position: absolute; left: 611px; top: 108px; font-family: "Days One", sans-serif; font-size: 26px; color: var(--section-title); text-transform: uppercase; letter-spacing: -.5px; }
  .carousel-arrow { position: absolute; top: 202px; width: 32px; height: 37px; }
  .carousel-arrow.prev { left: 558px; }
  .carousel-arrow.next { left: 1131px; }

  .thumb { position: absolute; top: 159px; height: 123px; background: var(--frame); padding: 6px; box-shadow: 0 1px 3px rgba(0,0,0,.15); }
  .thumb .photo { width: 100%; height: 100%; }
  .thumb-1 { left: 611px; width: 167px; }
  .thumb-2 { left: 784px; width: 161px; }
  .thumb-3 { left: 950px; width: 164px; }

  .photo-museum { background: linear-gradient(160deg, #2b3f86 0%, #8c9cc9 35%, #e6e6ea 55%, #1b2033 100%); }
  .photo-deck { background: linear-gradient(180deg, #f3f3f3 0%, #3b4a3c 30%, #b8763a 65%, #2a1e16 100%); }
  .photo-kitchen { background: linear-gradient(180deg, #4a3b33 0%, #9a5a44 45%, #d9c9b8 65%, #5a2d1c 100%); }

  .feature-card { position: absolute; left: 611px; top: 300px; width: 340px; height: 294px; background: linear-gradient(180deg, var(--card) 80%, rgba(220,220,220,.35)); }
  .feature-card .photo { position: absolute; left: 10px; top: 7px; width: 322px; height: 210px; }
  .feature-title { position: absolute; left: 8px; top: 230px; font-family: "Days One", sans-serif; font-size: 26px; color: #2f2f2f; text-transform: uppercase; letter-spacing: -.5px; }

  .feature-summary { position: absolute; left: 966px; top: 305px; width: 222px; font-size: 13.6px; line-height: 17.8px; color: var(--body-text); }
  .more-link { position: absolute; left: 965px; top: 474px; font-size: 14.2px; font-weight: bold; color: #2a2a2a; text-decoration: none; }

  .site-footer { position: absolute; left: 0; top: 653px; width: 1200px; height: 120px; background: var(--ink); }
  .site-footer p { position: absolute; left: 0; width: 1240px; top: 47px; text-align: center; font-size: 13px; color: var(--footer-text); }
</style>
</head>
<body>
<div class="page">
  <nav class="site-nav">
    <a class="is-active" href="#" style="left:143px">Home</a>
    <a href="#" style="left:278px">About</a>
    <a href="#" style="left:420px">Services</a>
    <a href="#" style="left:580px">Projects</a>
    <a href="#" style="left:745px">Contact Us</a>
    <div class="social-links" aria-label="Social links"><span></span><span></span><span></span><span></span></div>
  </nav>
  <div class="nav-pointer"></div>
  <div class="top-band"></div>

  <main class="main-panel"></main>

  <div class="brand">
    <span class="brand-mark"></span>
    <div class="brand-name">Vantor Loom<br>Design</div>
  </div>

  <h1 class="studio-title">Building Design &amp; Drafting Studio</h1>
  <p class="studio-intro">Providing a high&nbsp; quality and complete client service from concept design through Council planning approvals and building licenses to construction drawings for kitchens and bathrooms, extensions, additions, renovations and new homes.</p>

  <h2 class="section-title">Selected Work</h2>
  <svg class="carousel-arrow prev" viewBox="0 0 32 37" aria-label="Previous"><polygon points="32,0 32,37 0,18.5" fill="var(--arrow)"/></svg>
  <svg class="carousel-arrow next" viewBox="0 0 32 37" aria-label="Next"><polygon points="0,0 0,37 32,18.5" fill="var(--arrow)"/></svg>

  <div class="thumb thumb-1"><div class="photo photo-museum" role="img" aria-label="Cultural foundation building with curved shell facade at dusk"></div></div>
  <div class="thumb thumb-2"><div class="photo photo-deck" role="img" aria-label="Lit timber deck and steps of a house at night"></div></div>
  <div class="thumb thumb-3"><div class="photo photo-kitchen" role="img" aria-label="Modern kitchen with timber floor and brick splashback"></div></div>

  <article class="feature-card">
    <div class="photo photo-museum" role="img" aria-label="Cultural foundation building with curved shell facade reflected in water"></div>
    <h3 class="feature-title">Cultural Foundation</h3>
  </article>
  <p class="feature-summary">Lorem ipsum dolor sit amet, consectetur adipisicing elit, sed do eiusmod tempor incididunt ut labore et dolore magna aliqua. Ut enim ad minim veniam, quis nostrud exercitation ullamco laboris nisi ut aliquip ex ea commodo consequat.</p>
  <a class="more-link" href="#">more details</a>

  <div class="bottom-band"></div>
  <footer class="site-footer"><p>© 2013 Vantor Loom Design. All Rights Reserved</p></footer>
</div>
</body>
</html>
```